Software Product Website Design

We have a software product which we have just renamed from Milestone Linked Tracking (MLT) to Norvessa. The web site is for www.norvessa-example.com and needs to contain certain information related to our software product in accordance with the information contained in the previous product brochure (see attached). The logo file is also attached but the designer is free to propose alternative logo colours. The theme for the website must be based on the selected logo colours..
Target Market(s)
Project Management, Engineering, Construction etc companies involved with projects in all industries world-wide
Industry/Entity Type
Software
Coding
Coded - Design and coding required
Number of Pages Required
1 page
Font styles to use
Requirements
Must have
- Professional but exciting theme. The contents of the attached brochure should be included.

```html
<!DOCTYPE html>
<html lang="en">
<head>
<meta charset="utf-8">
<title>Norvessa — Milestone Linked Tracking</title>
<link rel="stylesheet" href="https://fonts.googleapis.com/css2?family=Roboto:wght@300;400;500;700&display=swap">
<style>
:root{
  --red:#d4202b;
  --red-dark:#b3161f;
  --blue:#1f3f9b;
  --ink:#333;
  --muted:#666;
  --light:#f3f4f6;
  --footer:#2b2b2b;
  --footer-bottom:#1e1e1e;
  --footer-text:#bdbdbd;
}
*{box-sizing:border-box;margin:0;padding:0}
html,body{width:791px;height:1200px;overflow:hidden}
body{font-family:"Roboto",Arial,sans-serif;color:var(--ink);background:#fff;position:relative}
.site-header{height:80px;display:flex;align-items:center;justify-content:space-between;padding:0 30px 0 82px;background:#fff}
.brand{display:flex;align-items:center;gap:8px;font-size:22px;font-weight:500;color:var(--blue)}
.brand-mark{width:18px;height:18px;background:var(--red)}
.main-nav{display:flex;gap:4px}
.main-nav a{font-size:11px;color:var(--ink);text-decoration:none;padding:8px 10px}
.main-nav a.active{background:var(--red);color:#fff}
.hero{position:relative;height:260px;background:linear-gradient(180deg,#f7f8fa,#e6e8ec);overflow:hidden}
.hero-visual{position:absolute;left:90px;top:28px;width:250px;height:210px;background:linear-gradient(180deg,#3b4048,#16181c);border-radius:4px}
.hero-copy{position:absolute;left:412px;top:98px;width:300px}
.hero-copy h2{font-size:21px;font-weight:500;color:var(--blue);margin-bottom:8px}
.hero-copy p{font-size:9px;line-height:1.5;color:var(--muted);margin-bottom:14px}
.btn{display:inline-block;background:var(--red);color:#fff;font-size:10px;font-weight:500;padding:7px 14px;text-decoration:none;border-radius:2px}
.slider-dots{display:flex;justify-content:center;gap:5px;margin-top:10px}
.slider-dots span{width:8px;height:8px;border-radius:50%;background:var(--blue)}
.slider-dots span.off{background:#b9c1d8}
.section-title{text-align:center;font-size:23px;font-weight:500;color:var(--ink)}
.title-rule{width:30px;height:2px;background:var(--red);margin:8px auto 0}
.welcome{padding-top:42px;text-align:center}
.welcome p{width:640px;margin:14px auto 18px;font-size:9px;line-height:1.55;color:var(--muted)}
.dashboard{margin:22px auto 0;width:370px;height:200px;background:linear-gradient(180deg,#dfe4ea,#f4f6f8);border:1px solid #cfd4da}
.testimonials{padding-top:64px;text-align:center}
.quote-mark{color:var(--red);font-size:14px;line-height:1;margin-top:4px}
.avatar{width:60px;height:60px;border-radius:50%;margin:6px auto 0;background:radial-gradient(circle,#e8c9a8,#b98c5e)}
.testimonials blockquote{width:560px;margin:12px auto 8px;font-size:9px;line-height:1.5;color:var(--muted)}
.client{font-size:11px;color:var(--red);font-style:italic}
.client small{font-size:8px;color:var(--muted)}
.site-footer{position:absolute;left:0;top:1043px;width:791px;height:122px;background:var(--footer);display:flex;padding:18px 40px 0 90px;gap:0}
.footer-col{width:160px}
.footer-col h4{color:#fff;font-size:12px;font-weight:500;margin-bottom:8px}
.footer-col li{list-style:none;font-size:8.5px;color:var(--footer-text);line-height:1.55}
.footer-col p{font-size:8.5px;color:var(--footer-text);line-height:1.55}
.newsletter{width:200px}
.subscribe{display:flex;margin-bottom:8px}
.subscribe span{flex:0 0 120px;height:20px;background:#fff;font-size:8px;color:#999;padding:5px 6px}
.subscribe b{height:20px;background:var(--red);color:#fff;font-size:8px;font-weight:500;padding:5px 10px}
.social{display:flex;gap:5px}
.social span{width:14px;height:14px;background:#3b6fc4;border-radius:2px}
.social span:last-child{background:#ddd}
.footer-bottom{position:absolute;left:0;top:1165px;width:791px;height:35px;background:var(--footer-bottom);display:flex;align-items:center;justify-content:center;font-size:8px;color:var(--footer-text)}
.footer-bottom .credit{position:absolute;right:40px}
</style>
</head>
<body>
<header class="site-header">
  <div class="brand"><span class="brand-mark"></span>Norvessa</div>
  <nav class="main-nav">
    <a class="active" href="#">Home</a><a href="#">About Us</a><a href="#">Products</a><a href="#">Services</a><a href="#">Operations</a><a href="#">Contact Us</a>
  </nav>
</header>

<section class="hero">
  <div class="hero-visual" role="img" aria-label="Desktop monitor showing Norvessa schedule charts"></div>
  <div class="hero-copy">
    <h2>Voluptatum deleniti atque</h2>
    <p>Track every milestone against the schedule in real time and see at a glance how progress affects delivery across all project phases.</p>
    <a class="btn" href="#">Learn More</a>
  </div>
</section>
<div class="slider-dots"><span></span><span></span><span></span><span class="off"></span></div>

<section class="welcome">
  <h2 class="section-title">Welcome To Our Website</h2>
  <div class="title-rule"></div>
  <p>Projects typically adopt critical path methodology (CPM) as a scheduling tool to develop interdependencies between work activities throughout all project phases. These activities are typically linked to form network diagrams that react to the effects of schedule progress. If activities are delayed or ahead of schedule, it is possible to assess their impact on the overall project schedule. These tools are invaluable for a project to monitor its performance relative to the critical contractual commitments.</p>
  <a class="btn" href="#">Learn More</a>
  <div class="dashboard" role="img" aria-label="Norvessa dashboard screenshot with milestone tables and charts"></div>
</section>

<section class="testimonials">
  <h2 class="section-title">Clients Testimonials</h2>
  <div class="quote-mark">&#8220;</div>
  <div class="avatar" role="img" aria-label="Client portrait"></div>
  <blockquote>Norvessa gave our team a clear view of every milestone. We now spot slippage weeks earlier and report progress to clients with confidence and far less manual effort each month.</blockquote>
  <div class="client">— Helena Marsh <small>Project Lead</small></div>
</section>

<footer class="site-footer">
  <div class="footer-col">
    <h4>Quick Links</h4>
    <ul><li>Home</li><li>About Us</li><li>Products</li><li>Services</li><li>Operations</li><li>Contact Us</li></ul>
  </div>
  <div class="footer-col">
    <h4>Contact Us</h4>
    <p>48 Harbor Line Road, Suite 210<br>Riverton<br>+1 (555) 014-2290<br>info@norvessa-example.com</p>
  </div>
  <div class="footer-col newsletter">
    <h4>Newsletter Subscribe</h4>
    <div class="subscribe"><span>Email address</span><b>Submit</b></div>
    <p>Receive product updates and release news in your inbox.</p>
  </div>
  <div class="footer-col">
    <h4>Follow Us</h4>
    <div class="social"><span></span><span></span><span></span><span></span></div>
  </div>
</footer>
<div class="footer-bottom">© 2015 www.norvessa-example.com | All Rights Reserved<span class="credit">Top ↑</span></div>
</body>
</html>
```